Multilingual Website for a Medico Company

We need a multilingual Website for our Medico company that sells gloves and masks, the website should have 3-5 subpages on 5 different languages.

Industry/Entity Type

Medtech

Number of Pages Required

5+ page

Requirements
Must have
• Unique Design - No template
Should not have
• No Templates

```html
<!DOCTYPE html>
<html lang="en">
<head>
<meta charset="utf-8">
<title>Curavo – Masks &amp; Gloves</title>
<link href="https://fonts.googleapis.com/css2?family=Montserrat:wght@500;600;700;800&family=Open+Sans:wght@400;600&display=swap" rel="stylesheet">
<style>
:root{
  --green-dark:#2c6a17;
  --green-deep:#1d4710;
  --lime:#84c916;
  --ink:#1b1b1b;
  --text:#3a3a3a;
  --card:#f4f4f4;
  --white:#fff;
}
*{margin:0;padding:0;box-sizing:border-box}
html,body{width:1200px;height:3114px;overflow:hidden;background:var(--white)}
body{position:relative;font-family:'Open Sans',sans-serif;color:var(--text)}
.abs{position:absolute}
h2{font-family:'Montserrat',sans-serif;font-weight:500;color:var(--ink)}
/* header */
.site-header{left:0;top:0;width:1200px;height:106px;border-bottom:1px solid #e5e5e5}
.brand{left:92px;top:22px;font-family:'Montserrat',sans-serif;font-weight:800;font-size:50px;color:var(--green-dark);display:flex;align-items:center;gap:12px}
.brand-dot{width:26px;height:26px;background:var(--lime);border-radius:50%}
.main-nav{left:537px;top:44px;display:flex;gap:40px;font-family:'Montserrat',sans-serif;font-weight:600;font-size:15px;color:#222}
.main-nav .active{color:var(--green-dark)}
.lang{left:967px;top:44px;font-family:'Montserrat',sans-serif;font-weight:600;font-size:15px;color:var(--green-dark)}
.cart{left:1035px;top:42px;display:flex;gap:10px;align-items:center;color:var(--green-dark);font-size:16px}
/* hero */
.hero{left:0;top:107px;width:1200px;height:530px;background:linear-gradient(180deg,#d9d6d0 0%,#cfccc6 60%,#c6c2bb 100%)}
.hero-brand{left:0;width:1200px;top:100px;text-align:center;font-family:'Montserrat',sans-serif;font-weight:800;font-size:110px;color:var(--green-dark)}
.hero-text{left:200px;width:800px;top:238px;text-align:center;font-size:22px;line-height:32px;color:#222}
.btn{display:inline-block;background:var(--green-dark);color:#fff;font-family:'Montserrat',sans-serif;font-weight:600;border-radius:30px;text-align:center}
.hero .btn{position:absolute;left:530px;top:328px;width:140px;height:46px;line-height:46px;font-size:16px}
/* sections */
.sec-title{font-size:37px}
.copy-block{display:flex;flex-direction:column;gap:11px;width:452px}
.body-copy{font-size:14.2px;line-height:30.5px;color:#333}
.about-photo{left:600px;top:722px;width:508px;height:323px;background:linear-gradient(135deg,#c98aa3,#b97893 60%,#a86b85);border-radius:0 80px 0 80px}
.why-photo{left:90px;top:1633px;width:508px;height:323px;background:linear-gradient(135deg,#9fb0b4,#8d7a6c 55%,#b0785c);border-radius:80px 0 80px 0}
.center{left:0;width:1200px;text-align:center}
.product{width:304px;height:354px;background:var(--card);border-radius:0 0 40px 0;top:1190px}
.product .pic{position:absolute;left:40px;top:50px;width:224px;height:160px;border-radius:20px}
.product h3{position:absolute;top:272px;width:100%;text-align:center;font-family:'Montserrat',sans-serif;font-weight:500;font-size:24px;color:var(--ink)}
.product a{position:absolute;top:310px;width:100%;text-align:center;font-size:15px;color:var(--green-dark);text-decoration:underline}
.testi{width:320px;height:246px;top:2125px;background:#fff;border-radius:0 0 40px 0;box-shadow:0 4px 16px rgba(0,0,0,.12);padding:50px 14px 0 34px;display:flex;flex-direction:column}
.quote-tab{position:absolute;left:36px;top:-26px;width:51px;height:51px;background:var(--lime);display:flex;align-items:center;justify-content:center}
.testi h3{font-family:'Montserrat',sans-serif;font-weight:500;font-size:24px;line-height:30px;color:var(--ink)}
.testi p{margin-top:16px;font-size:14.6px;line-height:28.5px;color:#444;white-space:nowrap}
.testi a{margin-top:16px;font-size:15px;font-weight:600;color:var(--lime);text-decoration:underline}
.arrow{top:2235px}
/* contact */
.contact-band{left:0;top:2456px;width:603px;height:556px;background:var(--lime)}
.start-band{left:603px;top:2456px;width:597px;height:556px;background:linear-gradient(135deg,#245514,#1a420d)}
.contact-band h2,.start-band h2{color:#fff;font-size:42px;font-weight:600}
.info{display:flex;gap:16px;align-items:center;color:#fff;font-family:'Montserrat',sans-serif;font-weight:600;font-size:15px;line-height:25px}
.ring{width:52px;height:52px;border:2px solid #fff;border-radius:50%;display:flex;align-items:center;justify-content:center;flex:none}
.social{display:flex;gap:18px}
.social span{width:14px;height:14px;background:#fff;border-radius:50%}
.field{background:#fff;font-size:14px;color:#555;padding:0 15px;line-height:44px;height:44px}
.submit{width:140px;height:46px;line-height:46px;background:var(--lime);color:#fff;font-size:17px}
/* footer */
.footer-nav{top:3047px;font-size:14px;color:#444;word-spacing:2px}
.footer-nav span{margin:0 16px}
.copy{top:3078px;font-size:13.5px;color:#555}
</style>
</head>
<body>

<header class="site-header abs">
  <div class="brand abs"><span class="brand-dot"></span>Curavo</div>
  <nav class="main-nav abs"><span class="active">Home</span><span>About Us</span><span>Products</span><span>Contact Us</span></nav>
  <div class="lang abs">En ⌄</div>
  <div class="cart abs">
    <svg width="22" height="18" viewBox="0 0 22 18" fill="none" stroke="#2c6a17" stroke-width="1.8"><path d="M1 2h4l3 10h10l2-7H7"/><circle cx="9" cy="16" r="1.2"/><circle cx="17" cy="16" r="1.2"/></svg>
    <span>$4.00</span>
  </div>
</header>

<section class="hero abs" role="img" aria-label="People wearing face masks standing against a pale wooden wall, looking at their phones">
  <div class="hero-brand abs">Curavo</div>
  <p class="hero-text abs">Lorem ipsum dolor sit amet, consectetur adipiscing elit, sed do eiusmod tempor incididunt ut labore et dolore magna aliqua.</p>
  <a class="btn">Buy Now</a>
</section>

<section class="about">
  <h2 class="sec-title abs" style="left:92px;top:738px">About Us</h2>
  <div class="copy-block abs" style="left:90px;top:800px">
    <p class="body-copy">Lorem ipsum dolor sit amet, consectetur adipiscing elit, sed do eiusmod tempor incididunt ut labore et dolore magna aliqua. Ut enim ad minim veniam, quis nostrud exercitation ullamco laboris nisi ut aliquip ex ea commodo consequat. Duis aute irure dolor in reprehenderit in voluptate velit esse cillum dolore eu fugiat nulla</p>
    <p class="body-copy">Lorem ipsum dolor sit amet, consectetur adipiscing elit, sed do eiusmod tempor incididunt ut labore et</p>
  </div>
  <div class="about-photo abs" role="img" aria-label="Woman in a winter hat and face mask pulling on white gloves against a pink wall"></div>
</section>

<section class="featured">
  <h2 class="sec-title abs center" style="top:1125px">Featured Products</h2>
  <div class="product abs" style="left:118px"><div class="pic" role="img" aria-label="Blue surgical face mask" style="background:linear-gradient(135deg,#8fd0ee,#4fa9db)"></div><h3>Product Name</h3><a>Buy Now</a></div>
  <div class="product abs" style="left:448px"><div class="pic" role="img" aria-label="Blue nitrile gloves with their box" style="background:linear-gradient(135deg,#a9c6ec,#3f78d0)"></div><h3>Product Name</h3><a>Buy Now</a></div>
  <div class="product abs" style="left:778px"><div class="pic" role="img" aria-label="Black reusable cloth face mask" style="background:linear-gradient(135deg,#4a4a4a,#151515)"></div><h3>Product Name</h3><a>Buy Now</a></div>
</section>

<section class="why">
  <div class="why-photo abs" role="img" aria-label="Woman in a face mask making a heart shape with her hands in front of a town street"></div>
  <h2 class="sec-title abs" style="left:670px;top:1650px">Why Us</h2>
  <div class="copy-block abs" style="left:668px;top:1711px">
    <p class="body-copy">Lorem ipsum dolor sit amet, consectetur adipiscing elit, sed do eiusmod tempor incididunt ut labore et dolore magna aliqua. Ut enim ad minim veniam, quis nostrud exercitation ullamco laboris nisi ut aliquip ex ea commodo consequat. Duis aute irure dolor in reprehenderit in voluptate velit esse cillum dolore eu fugiat nulla</p>
    <p class="body-copy">Lorem ipsum dolor sit amet, consectetur adipiscing elit, sed do eiusmod tempor incididunt ut labore et</p>
  </div>
</section>

<section class="testimonials">
  <h2 class="sec-title abs center" style="top:2033px">Testimonials</h2>
  <svg class="arrow abs" style="left:38px" width="12" height="20" viewBox="0 0 12 20" fill="none" stroke="#333" stroke-width="1.8"><path d="M10 2 2 10l8 8"/></svg>
  <svg class="arrow abs" style="left:1150px" width="12" height="20" viewBox="0 0 12 20" fill="none" stroke="#333" stroke-width="1.8"><path d="M2 2l8 8-8 8"/></svg>
  <article class="testi abs" style="left:88px">
    <div class="quote-tab"><svg width="26" height="20" viewBox="0 0 26 20" fill="#fff"><path d="M0 20V11Q0 3 8 0l2 3Q5 5 5 9h5v11zM14 20V11q0-8 8-11l2 3q-5 2-5 6h5v11z"/></svg></div>
    <h3>Mara Lind</h3><p>Lorem ipsum dolor sit amet, onsectetur<br>adipiscing elit, sed do eiusmod tempor<br>incididunt ut labore et dolore magna</p><a>Read More</a>
  </article>
  <article class="testi abs" style="left:439px">
    <div class="quote-tab"><svg width="26" height="20" viewBox="0 0 26 20" fill="#fff"><path d="M0 20V11Q0 3 8 0l2 3Q5 5 5 9h5v11zM14 20V11q0-8 8-11l2 3q-5 2-5 6h5v11z"/></svg></div>
    <h3>Tessa Holm</h3><p>Lorem ipsum dolor sit amet, onsectetur<br>adipiscing elit, sed do eiusmod tempor<br>incididunt ut labore et dolore magna</p><a>Read More</a>
  </article>
  <article class="testi abs" style="left:789px">
    <div class="quote-tab"><svg width="26" height="20" viewBox="0 0 26 20" fill="#fff"><path d="M0 20V11Q0 3 8 0l2 3Q5 5 5 9h5v11zM14 20V11q0-8 8-11l2 3q-5 2-5 6h5v11z"/></svg></div>
    <h3>Oren Vale</h3><p>Lorem ipsum dolor sit amet, onsectetur<br>adipiscing elit, sed do eiusmod tempor<br>incididunt ut labore et dolore magna</p><a>Read More</a>
  </article>
</section>

<section class="contact-band abs">
  <h2 class="abs" style="left:90px;top:62px">Contact Us</h2>
  <div class="info abs" style="left:92px;top:168px"><div class="ring"><svg width="20" height="18" viewBox="0 0 20 18" fill="#fff"><path d="M10 0 0 9h3v9h5v-6h4v6h5V9h3z"/></svg></div><div>Curavo.18 Linden Row,<br>PO Box 902,Alder,CO 80417</div></div>
  <div class="info abs" style="left:92px;top:251px"><div class="ring"><svg width="18" height="18" viewBox="0 0 24 24" fill="#fff"><path d="M6.6 10.8a15 15 0 0 0 6.6 6.6l2.2-2.2c.3-.3.7-.4 1-.2 1.1.4 2.3.6 3.6.6.6 0 1 .4 1 1V20c0 .6-.4 1-1 1A17 17 0 0 1 3 4c0-.6.4-1 1-1h3.5c.6 0 1 .4 1 1 0 1.3.2 2.5.6 3.6.1.3 0 .7-.2 1z"/></svg></div><div>Call Us :<br>555-204-3187</div></div>
  <div class="info abs" style="left:92px;top:330px"><div class="ring"><svg width="20" height="16" viewBox="0 0 20 16" fill="none" stroke="#fff" stroke-width="1.8"><rect x="1" y="1" width="18" height="14" rx="2"/><path d="m1 3 9 6 9-6"/></svg></div><div>Email Us<br>hello@curavo-care.com</div></div>
  <div class="social abs" style="left:96px;top:466px"><span></span><span></span></div>
</section>

<section class="start-band abs">
  <h2 class="abs" style="left:58px;top:62px">Let’s Get Started</h2>
  <p class="abs" style="left:58px;top:135px;width:420px;color:#fff;font-size:15px;line-height:27px">Lorem ipsum dolor sit amet, consectetur adipiscing elit, sed do eiusmod tempor incididunt ut labore et</p>
  <div class="field abs" style="left:59px;top:205px;width:204px">Name</div>
  <div class="field abs" style="left:274px;top:205px;width:204px">Phone No</div>
  <div class="field abs" style="left:59px;top:261px;width:204px">Email</div>
  <div class="field abs" style="left:274px;top:261px;width:204px">Address</div>
  <div class="field abs" style="left:59px;top:317px;width:419px;height:95px">Message</div>
  <div class="btn submit abs" style="left:59px;top:425px">Submit</div>
</section>

<footer>
  <nav class="footer-nav abs center">Home<span>|</span>About Us<span>|</span>Products<span>|</span>Contact Us</nav>
  <p class="copy abs center">Copyrights © 2020.All Rights Reserved</p>
</footer>

</body>
</html>
```